Postcard Design

I need to have a Table Tent made for our Restaurant. On one side is the Burger Specials and the other side is Happy Hour Drink specials. Our colors are black and white in the restaurant. We need a slightly larger font as our customers are older. The cost of the burgers is $13 each. we are an old school steak house.

Industry/Entity Type

Restaurant

```html
<!DOCTYPE html>
<html lang="en">
<head>
<meta charset="utf-8">
<title>Burger & Drink Specials Table Tent</title>
<link href="https://fonts.googleapis.com/css2?family=Alfa+Slab+One&family=Roboto+Slab:wght@800&family=Arimo:wght@400;700&display=swap" rel="stylesheet">
<style>
  :root{
    --lime:#b8d33b;
    --red:#d0161e;
    --red-deep:#a80f15;
    --cream:#fff4c2;
    --yellow:#ffe14a;
    --ink:#2a2a2a;
    --white:#ffffff;
  }
  html,body{margin:0;padding:0;overflow:hidden;}
  body{width:780px;height:1200px;background:var(--lime);}
  .table-tent{position:relative;width:780px;height:1200px;overflow:hidden;background:var(--lime);}
  .frame-shapes{position:absolute;inset:0;}
  .burger-photo{position:absolute;left:440px;top:0;width:340px;height:595px;}
  .drinks-photo{position:absolute;left:390px;top:930px;width:385px;height:258px;}

  .burger-list{position:absolute;left:40px;top:50px;width:400px;margin:0;padding:0;list-style:none;}
  .burger-item{margin:0 0 12px;}
  .burger-name{font-family:"Roboto Slab",serif;font-weight:800;font-size:18px;line-height:24px;color:var(--red);margin:0;}
  .burger-desc{font-family:"Arimo",sans-serif;font-size:16px;line-height:20px;color:var(--ink);margin:0;}

  .price-note{position:absolute;left:40px;top:478px;margin:0;font-family:"Alfa Slab One",serif;font-size:36px;line-height:40px;color:var(--red-deep);}
  .price-badge{position:absolute;left:297px;top:462px;width:126px;height:126px;border-radius:50%;background:var(--red);border:5px solid var(--white);box-sizing:border-box;
    display:flex;align-items:center;justify-content:center;font-family:"Alfa Slab One",serif;font-size:54px;color:var(--white);box-shadow:0 3px 6px rgba(0,0,0,.3);}
  .price-badge sup{font-size:28px;margin-right:2px;}

  .drink-panel{position:absolute;left:20px;top:618px;width:356px;height:562px;background:linear-gradient(180deg,var(--red) 0%,var(--red-deep) 100%);box-sizing:border-box;padding:14px 18px 0;}
  .drink-title{margin:0 0 12px;font-family:"Alfa Slab One",serif;font-size:31px;line-height:40px;white-space:nowrap;color:var(--cream);text-shadow:3px 3px 0 #5a0a0c;}
  .drink-day{font-family:"Arimo",sans-serif;font-size:15px;line-height:19px;color:var(--white);padding:7px 0;border-top:1px solid rgba(255,255,255,.45);margin:0;}
  .drink-title + .drink-day{border-top:none;padding-top:0;}
  .day-name,.day-strong{font-weight:700;}
  .drink-footer{position:absolute;left:18px;right:18px;bottom:34px;margin:0;text-align:center;font-family:"Arimo",sans-serif;font-weight:700;font-size:16px;line-height:22px;color:var(--yellow);}
</style>
</head>
<body>
<main class="table-tent">
  <svg class="frame-shapes" width="780" height="1200" viewBox="0 0 780 1200">
    <defs>
      <linearGradient id="lowerGlow" x1="0" y1="0" x2="0" y2="1">
        <stop offset="0" stop-color="#ffffff"/>
        <stop offset="1" stop-color="#eef4d2"/>
      </linearGradient>
    </defs>
    <path d="M12 12 H620 Q720 8 768 60 V420 Q560 420 400 448 Q220 480 12 462 Z" fill="#ffffff"/>
    <path d="M12 600 H768 V1188 H12 Z" fill="url(#lowerGlow)"/>
  </svg>

  <svg class="burger-photo" viewBox="0 0 340 595" role="img" aria-label="Photo of a tall cheeseburger with sesame bun, beef patty, cheese, tomato, onion and lettuce">
    <defs>
      <linearGradient id="burgerTone" x1="0" y1="0" x2="0" y2="1">
        <stop offset="0" stop-color="#d89a4a"/>
        <stop offset="0.45" stop-color="#6b3a22"/>
        <stop offset="0.65" stop-color="#d9382c"/>
        <stop offset="0.85" stop-color="#7fb53a"/>
        <stop offset="1" stop-color="#d9a25a"/>
      </linearGradient>
    </defs>
    <ellipse cx="175" cy="298" rx="165" ry="290" fill="url(#burgerTone)"/>
  </svg>

  <ul class="burger-list">
    <li class="burger-item"><h2 class="burger-name">BBQ Bacon Burger</h2><p class="burger-desc">Bacon, cheddar, onion rings, bbq sauce,<br>lettuce, tomato and your choice of side.</p></li>
    <li class="burger-item"><h2 class="burger-name">Green Chile Burger</h2><p class="burger-desc">mustard, pickles, tomato, onions, american cheese,<br>hatch green chile, and your choice of side</p></li>
    <li class="burger-item"><h2 class="burger-name">Grilled Chicken BLT</h2><p class="burger-desc">grilled chicken, mozzarella, bacon, lettuce,<br>tomato, mayo and your choice of side</p></li>
    <li class="burger-item"><h2 class="burger-name">Jumbo Shrimp</h2><p class="burger-desc">Stuffed with pepper jack cheese, jalapeño and<br>wrapped in bacon.</p></li>
    <li class="burger-item"><h2 class="burger-name">No Carb Burger</h2><p class="burger-desc">Lettuce leaves as your bun, meat patty,<br>cheese if you like, lettuce, tomato, onions,<br>mayo, mustard and your choice of side</p></li>
  </ul>

  <p class="price-note">The above<br>items are</p>
  <div class="price-badge"><sup>$</sup>13</div>

  <section class="drink-panel">
    <h1 class="drink-title">DRINK SPECIALS</h1>
    <p class="drink-day"><span class="day-name">MONDAY</span><br>All well drinks $4<br>from 5 PM to 7PM</p>
    <p class="drink-day"><span class="day-name">TUESDAY</span><br>Cosmopolitan $4<br>from 5PM to 7PM</p>
    <p class="drink-day"><span class="day-name">WEDNESDAY</span> - 1/2 price glasses<br>of wine from 5 PM to 7 PM only<br><span class="day-strong">JOIN US AFTER</span> 7 PM for<br>1/2 price wine bottles</p>
    <p class="drink-day"><span class="day-name">THURSDAY</span> - $4 Martinis<br>from 5 PM to 7 PM</p>
    <p class="drink-day"><span class="day-name">FRIDAY</span> - $4 Margaritas<br>from 5 PM to 7 PM<br>1/2 price appetizers<br>from 5 PM to 7PM</p>
    <p class="drink-footer">1/2 PRICED FROM 5PM TO 7 PM<br>MONDAY TO FRIDAY.</p>
  </section>

  <svg class="drinks-photo" viewBox="0 0 385 258" role="img" aria-label="Photo of assorted cocktails, a beer and a martini with lime garnish">
    <defs>
      <linearGradient id="drinkTone" x1="0" y1="0" x2="1" y2="0">
        <stop offset="0" stop-color="#d7e9f2"/>
        <stop offset="0.4" stop-color="#7fc6e6"/>
        <stop offset="0.7" stop-color="#f2b431"/>
        <stop offset="1" stop-color="#c9e0a0"/>
      </linearGradient>
    </defs>
    <rect x="5" y="10" width="375" height="245" rx="30" fill="url(#drinkTone)" opacity="0.85"/>
  </svg>
</main>
</body>
</html>
```